Im open to ideas.. I was thinking on my business cards aswell as my logo. a place for my name. email. phone number and abn..

ive attched a file with my business logo. which i dont love the colours.. i was think a dark background with charcoal letters so something along those colour schumes but im open to ideas..

Business

BRL Constructions

```html
<!DOCTYPE html>
<html lang="en">
<head>
<meta charset="utf-8">
<title>BRL Constructions – Business Cards</title>
<link rel="stylesheet" href="https://fonts.googleapis.com/css2?family=Arimo:wght@400;700&display=swap">
<style>
  :root {
    --backdrop: #3a322e;
    --card: #141414;
    --card-edge: #1e1e1e;
    --silver: #9a9a9a;
    --white: #f4f4f4;
    --soft-white: #d8d8d8;
    --accent: #e0201c;
    --rule: #8a8a8a;
  }
  * { margin: 0; padding: 0; box-sizing: border-box; }
  html, body { width: 1200px; height: 787px; overflow: hidden; }
  body {
    background: var(--backdrop);
    font-family: "Arimo", Arial, sans-serif;
    display: flex;
    align-items: center;
    justify-content: center;
    gap: 60px;
  }
  .card {
    width: 525px;
    height: 300px;
    background: var(--card);
    border: 1px solid var(--card-edge);
    border-radius: 3px;
    box-shadow: 0 10px 30px rgba(0,0,0,.45);
    position: relative;
  }
  .wordmark {
    font-weight: 700;
    text-transform: uppercase;
    letter-spacing: 1px;
    display: flex;
    align-items: center;
    gap: 12px;
  }
  .wordmark-square {
    width: 18px; height: 18px;
    background: currentColor;
  }
  /* back */
  .card-back {
    display: flex;
    flex-direction: column;
    align-items: center;
    justify-content: center;
    gap: 34px;
  }
  .card-back .wordmark { color: var(--silver); font-size: 38px; }
  .website {
    color: var(--soft-white);
    font-size: 14px;
    letter-spacing: 4px;
  }
  /* front */
  .card-front .wordmark {
    position: absolute;
    top: 78px; right: 40px;
    color: var(--white);
    font-size: 34px;
  }
  .card-front .wordmark-square { background: var(--accent); }
  .holder {
    position: absolute;
    left: 40px; top: 196px;
    width: 120px;
    text-align: right;
  }
  .holder-name { color: var(--accent); font-size: 17px; }
  .holder-role { color: var(--white); font-size: 16px; margin-top: 4px; }
  .divider {
    position: absolute;
    left: 178px; top: 192px;
    width: 1px; height: 78px;
    background: var(--rule);
  }
  .contact {
    position: absolute;
    left: 196px; top: 192px;
    list-style: none;
    color: var(--soft-white);
    font-size: 15px;
  }
  .contact li { display: flex; align-items: center; gap: 10px; height: 26px; }
  .contact .abn { padding-left: 0; }
  .contact svg { width: 15px; height: 15px; fill: var(--accent); }
</style>
</head>
<body>
  <section class="card card-back" aria-label="Card back">
    <div class="wordmark"><span class="wordmark-square"></span>BRL Constructions</div>
    <p class="website">www.brlbuild.com</p>
  </section>

  <section class="card card-front" aria-label="Card front">
    <div class="wordmark"><span class="wordmark-square"></span>BRL Constructions</div>
    <div class="holder">
      <p class="holder-name">Sam Porter</p>
      <p class="holder-role">President</p>
    </div>
    <span class="divider"></span>
    <ul class="contact">
      <li class="abn">ABN: 987654321</li>
      <li>
        <svg viewBox="0 0 16 16" aria-hidden="true"><path d="M2 6c0-2 2-3 6-3s6 1 6 3v1h-3V5.5H5V7H2z"/><path d="M4 8h8l1.5 5h-11z"/></svg>
        555 0142 7788
      </li>
      <li>
        <svg viewBox="0 0 16 16" aria-hidden="true"><path d="M1 3h14v10H1z M2.2 4l5.8 4.6L13.8 4z" fill-rule="evenodd"/></svg>
        sam@brlbuild.com
      </li>
    </ul>
  </section>
</body>
</html>
```